Flyer redesign

We need this flier {Seasonal Care back 2018} redesigned for our 2019 season. It is attached below. New design should look different from current design. Be creative yet still professional.

Requirements
Must have
• Designed in photoshop.
• Should have the same text as current design. Only is "2019" instead of 2018. We want a different look with same info to send our customers next year.
• size: standard letter paper 8.5" x 11"
Nice to have
• Can use optional images provided. Not required though. See our website for more photos. thornbrookmemorial.org. send message through briskdrafts if you want a specific photo.
Should not have
• Do not take current design and just change date or image. Make the design look different.

```html
<!DOCTYPE html>
<html lang="en">
<head>
<meta charset="utf-8">
<title>Thornbrook Memorial – 2019 Gravesite Landscaping Packages</title>
<link rel="stylesheet" href="https://fonts.googleapis.com/css2?family=PT+Sans:wght@400;700&display=swap">
<style>
:root{
  --navy:#173f78;
  --blue:#2a62a6;
  --sky:#5f8fcb;
  --gold:#e8b830;
  --olive:#a49a5c;
  --olive-dark:#8e844b;
  --maroon:#7a1b1d;
  --cream:#efe7c6;
  --ink:#1d1d1d;
  --white:#ffffff;
}
*{box-sizing:border-box;margin:0;padding:0}
html,body{width:927px;height:1200px;overflow:hidden;background:var(--white)}
body{font-family:"PT Sans",Arial,sans-serif;color:var(--ink)}
.flyer{position:relative;width:927px;height:1200px;overflow:hidden;background:var(--white)}

.hero-photo{position:absolute;left:0;top:0;width:927px;height:560px;
  background:linear-gradient(180deg,#cfd8c9 0%,#9fb08a 35%,#6f8a5a 60%,#b8bcb4 80%,#d9dbd6 100%)}
.top-band{position:absolute;left:0;top:0;width:927px;height:80px}
.brand{position:absolute;top:22px;left:0;width:927px;display:flex;justify-content:center;align-items:center;gap:12px}
.brand-mark{width:30px;height:30px;border-radius:50%;background:var(--white);border:2px solid var(--navy)}
.brand-name{font-size:27px;font-weight:700;color:var(--maroon);letter-spacing:1px}

.title-disc{position:absolute;left:-110px;top:170px;width:400px;height:400px;border-radius:50%;
  background:rgba(255,255,255,.86);border:14px solid var(--navy);box-shadow:0 0 0 4px rgba(255,255,255,.6)}
.title{position:absolute;left:14px;top:230px;width:220px;text-align:center;color:var(--maroon);line-height:1.08}
.title-year{font-size:62px;display:block;margin-bottom:4px}
.title-line{font-size:37px;display:block}

.lower-bg{position:absolute;left:0;top:540px;width:927px;height:660px}

.package{position:absolute;top:550px;width:292px}
.package-seasonal{left:12px}
.package-basic{left:320px}
.package-perpetual{left:625px}
.package-tab{height:126px;background:linear-gradient(180deg,var(--olive),var(--olive-dark));
  border-radius:6px 6px 0 0;text-align:center;padding-top:10px;box-shadow:0 3px 6px rgba(0,0,0,.3)}
.package-name{font-size:26px;line-height:1.05;color:var(--maroon);text-transform:uppercase;font-weight:400}
.package-tagline{font-size:17px;line-height:1.2;color:var(--cream);margin-top:12px;padding:0 18px}
.package-card{height:450px;background:var(--white);padding:18px 16px 0 16px;box-shadow:0 4px 10px rgba(0,0,0,.35);position:relative}
.features{list-style:none}
.features li{position:relative;padding-left:22px;font-size:17px;line-height:1.2;margin-bottom:8px}
.features li::before{content:"";position:absolute;left:0;top:3px;width:13px;height:13px;border-radius:50%;background:var(--maroon)}
.features li::after{content:"";position:absolute;left:3px;top:7px;width:4px;height:4px;border-right:2px solid var(--white);border-top:2px solid var(--white);transform:rotate(45deg)}
.features li.plain{padding-left:22px}
.features li.plain::before,.features li.plain::after{display:none}
.features.tight li{margin-bottom:4px}

.rates{margin:70px 0 0 14px;color:var(--maroon)}
.rate-term{font-size:19px;display:block;line-height:1}
.rate-price{font-size:39px;display:block;line-height:1;margin-bottom:4px}
.rates-note{font-size:17px;margin:12px 0 0 14px;line-height:1.2}

.payment{text-align:center;color:var(--maroon)}
.payment-label{font-size:19px;color:var(--ink);line-height:1.15;display:block}
.payment-price{font-size:31px;display:block;margin-top:4px}
.payment-basic{margin-top:72px}
.payment-perpetual{margin-top:0}
.fine-print{font-size:16px;line-height:1.2;margin-top:14px;text-align:left;color:var(--ink)}
.package-basic .fine-print{margin-left:14px}

.footer{position:absolute;left:0;top:1152px;width:927px;display:flex;justify-content:space-between;padding:0 32px;color:var(--white);font-size:17px}
</style>
</head>
<body>
<main class="flyer">
  <div class="hero-photo" role="img" aria-label="Photograph of a cemetery path lined with headstones, trimmed green hedges and trees"></div>

  <svg class="top-band" viewBox="0 0 927 80" aria-hidden="true">
    <path d="M0 0H927V30Q700 58 463 58Q230 58 0 22Z" fill="var(--navy)"/>
    <path d="M0 22Q230 58 463 58Q700 58 927 30V40Q700 70 463 70Q230 70 0 32Z" fill="var(--gold)"/>
    <path d="M0 32Q230 70 463 70Q700 70 927 40V46Q700 78 463 78Q230 78 0 38Z" fill="var(--white)"/>
  </svg>
  <div class="brand">
    <span class="brand-mark"></span>
    <span class="brand-name">THORNBROOK MEMORIAL</span>
  </div>

  <svg class="lower-bg" viewBox="0 0 927 660" aria-hidden="true">
    <defs>
      <linearGradient id="lowerBlue" x1="0" y1="0" x2="0" y2="1">
        <stop offset="0" stop-color="var(--sky)"/>
        <stop offset="0.5" stop-color="var(--blue)"/>
        <stop offset="1" stop-color="var(--navy)"/>
      </linearGradient>
    </defs>
    <rect x="0" y="0" width="927" height="660" fill="url(#lowerBlue)"/>
    <path d="M0 560Q460 470 927 520V660H0Z" fill="var(--navy)"/>
    <path d="M300 545Q620 480 927 500V512Q620 494 300 552Z" fill="var(--gold)"/>
  </svg>

  <div class="title-disc"></div>
  <h1 class="title">
    <span class="title-year">2019</span>
    <span class="title-line">Gravesite</span>
    <span class="title-line">Landscaping</span>
    <span class="title-line">Packages</span>
  </h1>

  <section class="package package-seasonal">
    <div class="package-tab">
      <h2 class="package-name">Seasonal<br>Care</h2>
      <p class="package-tagline">Seasonal landscaping grave care.</p>
    </div>
    <div class="package-card">
      <ul class="features">
        <li>Weeding and trimming service on your gravesite approximately every 7 weeks during the growing season: mid-April through mid-October</li>
      </ul>
      <div class="rates">
        <span class="rate-term">3 YEARS</span><span class="rate-price">$327</span>
        <span class="rate-term">2 YEARS</span><span class="rate-price">$218</span>
        <span class="rate-term">1YEAR</span><span class="rate-price">$109</span>
      </div>
      <p class="rates-note">Multi-year payment locks in current rates.</p>
    </div>
  </section>

  <section class="package package-basic">
    <div class="package-tab">
      <h2 class="package-name">Basic Care<br>Endowment</h2>
      <p class="package-tagline">Landscaping care forever for graves with no plantings</p>
    </div>
    <div class="package-card">
      <ul class="features">
        <li>Weeding and trimming services on your gravesite 2 times per year: mid-May and mid-September Monument leveling</li>
        <li>Payment ensures grave care forever</li>
      </ul>
      <div class="payment payment-basic">
        <span class="payment-label">12 MONTHLY<br>PAYMENT OF</span>
        <span class="payment-price">$225.00*</span>
      </div>
      <p class="fine-print">*gravesite with single headstones.Call for other monument types and single payment discount.<br>Valid through 10/31/2019</p>
    </div>
  </section>

  <section class="package package-perpetual">
    <div class="package-tab">
      <h2 class="package-name">Perpetual Care<br>Endowement</h2>
      <p class="package-tagline">Landscaping care forever for graves with plantings.</p>
    </div>
    <div class="package-card">
      <ul class="features tight">
        <li>Weeding and trimming services on your gravesite approximately every 7 weeks during the growing season: mid-April through mid-October</li>
        <li>Monument leveling and Cleaning</li>
        <li>Payment ensures grave care forever</li>
        <li>Full bed of boxwood shrubs</li>
        <li>Replacement of shrubs</li>
        <li>Trust certificate</li>
      </ul>
      <div class="payment payment-perpetual">
        <span class="payment-label">12 MONTHLY<br>PAYMENTS OF</span>
        <span class="payment-price">$280.42</span>
      </div>
      <p class="fine-print">Call for single payment discount. Valid through 10/31/2019.</p>
    </div>
  </section>

  <footer class="footer">
    <span>info@thornbrookmemorial.org</span>
    <span>(555) 014-2290</span>
    <span>www.thornbrookmemorial.com</span>
  </footer>
</main>
</body>
</html>
```